Trifold Brochure

This is relatively easy. We already have a trifold made we simply want to update the LOOK to look more like our current website. All content would stay the same the only thing that would change would be the fonts, colors and background images to match the current website.

I have attached a word doc of the old trifold brochure. We would want the content to remain on the same pages of the trifold. Again all you are doing is updating the font, logo, colors and any background images. Please comment with any questions.

This is a 5 day project!

Requirements
Must have
• Logo, colors and fonts to match our current website.
http://www.brambleworksgroup.example/

```html
<!DOCTYPE html>
<html lang="en">
<head>
<meta charset="utf-8">
<title>Piling System Trifold</title>
<link href="https://fonts.googleapis.com/css2?family=Montserrat:wght@500;600&family=Questrial&display=swap" rel="stylesheet">
<style>
:root{
  --field-dark:#3f5a1f;
  --field:#55732c;
  --field-light:#6a8a38;
  --panel:#ffffff;
  --ink:#2b2b2b;
  --accent:#4f6b22;
  --rule:#5d7a2e;
  --figure-a:#ece6d2;
  --figure-b:#a39c86;
}
*{margin:0;padding:0;box-sizing:border-box}
html,body{width:1200px;height:928px;overflow:hidden}
body{
  position:relative;
  background:radial-gradient(ellipse at 50% 45%,var(--field-light) 0%,var(--field) 55%,var(--field-dark) 100%);
  font-family:"Questrial",sans-serif;
  color:var(--ink);
}
.panel{
  position:absolute;top:25px;height:880px;
  background:var(--panel);border-radius:32px;
}
.panel--includes{left:28px;width:375px;padding:30px 22px 0 26px}
.panel--system{left:431px;width:375px;padding:36px 30px 0 32px}
.panel--standards{left:834px;width:348px;padding:30px 26px 0 34px}

.label{font-family:"Montserrat",sans-serif;font-weight:600;font-size:11.5px;color:var(--accent);letter-spacing:.2px}
.checklist{list-style:none;margin-top:28px}
.checklist li{position:relative;padding-left:22px;font-size:12.3px;line-height:21px;margin-bottom:0}
.checklist li::before{content:"\2713";position:absolute;left:2px;top:0;font-size:12px}
.flex-label{margin-top:30px}
.flex-text{font-size:12.3px;line-height:21px;margin-top:6px}
.figure{
  position:absolute;left:85px;top:535px;width:185px;height:328px;border-radius:14px;
  background:linear-gradient(160deg,var(--figure-a) 0%,#cfc7ae 45%,var(--figure-b) 100%);
}

.panel--system p,.panel--system h3{font-size:10.9px;line-height:14.7px}
.panel--system p{margin-bottom:14px}
.panel--system h3{font-family:"Montserrat",sans-serif;font-weight:500;color:var(--accent);font-size:10px;letter-spacing:.4px;margin:2px 0 5px}

.panel--standards h2{font-family:"Montserrat",sans-serif;font-weight:600;color:var(--accent);font-size:16.5px;line-height:31px}
.notes{margin-top:8px;padding-left:14px;font-size:11.2px;line-height:19.2px}
.notes li{padding-left:4px}
.notes ol{list-style:lower-alpha;padding-left:14px}
.contact{position:absolute;left:56px;right:56px;top:703px;border-top:1.5px solid var(--rule);border-bottom:1.5px solid var(--rule);padding:12px 0 16px;text-align:center;font-size:11px;line-height:19.5px;color:var(--accent)}
</style>
</head>
<body>
<section class="panel panel--includes">
  <div class="label">Our System includes:</div>
  <ul class="checklist">
    <li>Collar cut to customer length in sizes ranging from 12" to 144".</li>
    <li>Collar Cap with galvanized steel u-bolts to connect to the structure.</li>
    <li>Collar spacers to allow for variations in Piling diameter</li>
    <li>Collar Cap spacers to allow for variations in piling diameter.</li>
    <li>Tubes of high strength adhesive glue to connect the Piling to the Collar and for the Collar flange and to fill gaps between the Piling and the Collar due to the nature of irregular Pilings.</li>
    <li>Detailed installation manual providing guidance to the installation contractor.</li>
    <li>Detailed written specifications provided in paper format and available in word format upon request.</li>
  </ul>
  <div class="label flex-label">Flexibility:</div>
  <p class="flex-text">Our system has been designed to accommodate piles ranging in diameter from 8" to 12". The system can also correct vertical alignments by up to 6 degrees.</p>
  <div class="figure" role="img" aria-label="Exploded rendering of the collar halves, spacers and collar cap around a piling"></div>
</section>

<section class="panel panel--system">
  <p>Our Patented Piling system has been designed to withstand the corrosive environment of beach communities. The salt water and windblown sand corrodes unprotected materials, and yes, even stainless steel. Our system utilizes a high strength carbon fiber material that is corrosion proof from salt water and UV proof. The system will not erode, decay or loose strength over time. The system has three installation conditions, for raising a house on existing pilings, repairing damaged pilings, and for connecting new pilings to floor joists in new construction. The three options are generally described below:</p>
  <h3>RAISING A STRUCTURE</h3>
  <p>A house on pilings can be raised by disconnecting the house from the pilings, raise the house to create a work area, cut all of the piles to a preset elevation, and install the Collar on the piling. The Collar is connected to the piling by six galvanized lag bolts and is glued with a high strength adhesive and all gaps are filled with flowable epoxy fill and fiber. The Collar extends above the piling to the bottom of the home's joists to the preset height, up to 6'-6", or higher when lateral supports are considered. Once the Collar is set on the home, it is filled with concrete to transfer the load of the house from the floor joists directly to the top of the piling, the concrete provides the compressive strength, while the Collar provides tensile and shear strength. A Collar Cap is then installed with two galvanized steel u-bolts which extend into the floor joists for the installer to connect to the joists.</p>
  <h3>PILING REPAIRS AND EXTENSIONS</h3>
  <p>A 36" section of Collar can be installed onto an existing piling and a new section of piling can be placed on top, with 18" of the Collar covering the top of the existing and 18" covering the bottom of the new piling. Generally, the minimum length of the new piling needs to be 6 feet to ensure the piling length is not too short, which could lead to reduced piling loading capacity. This option generally requires lateral support of the pilings. Consult with your design professional</p>
  <h3>NEW CONSTRUCTION</h3>
  <p>The standard practice for connecting pilings to floor joists is to notch the pilings and bolt the joists to the pilings. This method dramatically reduces the strength of the piling due to reduced cross sectional area at the connection point. Additionally, this connection method exposes more surface area of the piling allowing for additional potential for dry rot. A 12" Collar section with a Collar Cap can be used to connect directly to the top of the new piling providing a connection that will outlast the piling by literally thousands of years.</p>
</section>

<section class="panel panel--standards">
  <h2>General Performance Standards,<br>Notes and Guidance:</h2>
  <ol class="notes">
    <li>General Performance Standards:
      <ol>
        <li>Vertical loading (vertical compression) 90 Kips</li>
        <li>Bending moment 65 ft-Kips</li>
        <li>Shear (lateral forces) 10 Kips.</li>
        <li>Alignment/plumpness correction 6 Deg.</li>
      </ol>
    </li>
    <li>This document and information provided is the property of BWG and shall not be altered, used or referenced by any third party without the expressed written permission of BWG.</li>
    <li>The User of this system is advised that they should obtain services of a design professional for the use of this product. BWG only represents that our product will withstand loading as documented in our specifications. The design professional shall evaluate the loading conditions and determine if the loading conditions fall within the parameters of the Collar system. Additionally, the user should employ the design professional to inspect the Pilings to ensure they are acceptable for use.</li>
    <li>Local Permitting may be required for use of this product. Consult with your local code official prior to use.</li>
    <li>The User of this system should employ installation contractors that have adequate skills for the required work. BWG does not and cannot attest to any skill set or quality of work of any installer.</li>
    <li>The written instructions for installation must be followed. Failure to do so could result in failure of the system.</li>
  </ol>
  <address class="contact" style="font-style:normal">
    PO Box 41180,<br>
    Millbrook Valley, PA 18900-0410<br>
    T. 555. 402.7813 &nbsp;|&nbsp; F. 555.219.0644<br>
    Email: sales@brambleworksgroup.example<br>
    www.brambleworksgroup.example
  </address>
</section>
</body>
</html>
```